Pellrow Strategies business card

I need a business card for my new strategic consulting LLC, Pellrow Strategies. We specialize in helping people who care about broadband technology and telecommunications policy, and we're based in Washington DC. I'm looking for a card that says smart, credible, future-facing and signals a high level of expertise. It's DC, so there's clearly a limit to how crazy we can go with this card, but I am looking for a design that reflects a company that is comfortable with technology, policy, and having a little bit fun. I'm uploading my logo below, and I'd like to have it be part of the card design in some fashion.
Target Market(s)
Telecommunications and technology policy professionals
Industry/Entity Type
Technology policy
Contact Information for Business Card
Name of business, my name (Colin Mabberly), email (colin@pellrowstrategies.example) , phone number (202-555-0148)phone number
Look and feel

```html
<!DOCTYPE html>
<html lang="en">
<head>
<meta charset="utf-8">
<title>Pellrow Strategies – Business Card</title>
<link rel="stylesheet" href="https://fonts.googleapis.com/css2?family=Inter:wght@400;700&display=swap">
<style>
  :root {
    --backdrop: #d8d8d8;
    --card: #fcfcf7;
    --brand-blue: #1a56a0;
    --ink-navy: #0f2d54;
    --rule: #c8d6ea;
    --route-light: #dfe8f4;
    --label: #1d1d1d;
  }
  * { box-sizing: border-box; margin: 0; padding: 0; }
  html, body { width: 1200px; height: 692px; overflow: hidden; }
  body {
    background: var(--backdrop);
    font-family: "Inter", Arial, sans-serif;
    position: relative;
  }
  .side-label {
    position: absolute;
    left: 0; width: 1200px;
    text-align: center;
    font-size: 20px;
    line-height: 24px;
    color: var(--label);
    letter-spacing: 0.5px;
  }
  .side-label--front { top: 17px; }
  .side-label--back { top: 661px; }

  .card {
    position: absolute;
    left: 333px;
    width: 530px;
    background: var(--card);
    overflow: hidden;
  }
  .card--front { top: 50px; height: 281px; }
  .card--back { top: 361px; height: 295px; }

  /* Front */
  .brand-name {
    position: absolute;
    left: 0; right: 0; top: 112px;
    text-align: center;
    font-weight: 700;
    font-size: 48px;
    line-height: 58px;
    color: var(--brand-blue);
    letter-spacing: -0.5px;
    white-space: nowrap;
  }
  .front-band {
    position: absolute;
    left: 0; right: 0; bottom: 0;
    height: 4px;
    background: var(--brand-blue);
  }

  /* Back */
  .route-art {
    position: absolute;
    right: 0; top: 0;
    width: 150px; height: 295px;
    background: linear-gradient(200deg, var(--route-light) 0%, rgba(223,232,244,0.35) 60%, rgba(252,252,247,0) 100%);
  }
  .contact {
    position: absolute;
    left: 0; right: 0; top: 59px;
    text-align: center;
    color: var(--ink-navy);
    white-space: nowrap;
  }
  .contact__name {
    font-weight: 700;
    font-size: 42px;
    line-height: 46px;
    letter-spacing: -0.4px;
  }
  .contact__company {
    font-size: 28px;
    line-height: 34px;
    margin-top: 2px;
  }
  .contact__rule {
    width: 120px;
    height: 1px;
    background: var(--rule);
    margin: 16px auto;
  }
  .contact__line {
    font-size: 28px;
    line-height: 33px;
  }
</style>
</head>
<body>
  <div class="side-label side-label--front">FRONT</div>

  <section class="card card--front">
    <div class="brand-name">Pellrow Strategies</div>
    <div class="front-band"></div>
  </section>

  <section class="card card--back">
    <div class="route-art" role="img" aria-label="Faint line drawing of winding roads and map routes in pale blue"></div>
    <div class="contact">
      <div class="contact__name">Colin Mabberly</div>
      <div class="contact__company">Pellrow Strategies</div>
      <div class="contact__rule"></div>
      <div class="contact__line">colin@pellrowstrategies.example</div>
      <div class="contact__line">202-555-0148</div>
    </div>
  </section>

  <div class="side-label side-label--back">BACK</div>
</body>
</html>
```